LA's Newest HEMP Facial Oil and Body Oil Packaging Project

We need a packaging concept for a Hemp based facial oil and body oil. We need label design for the bottle and carton graphics. I am attaching a few reference photos. The target demographic is women between 17-35 year old. Products need to be able to stand out in crowded stores with clear calls to action.
1oz Dropper Bottle with Unit Carton - Hemp Facial Oil
4oz PET Bottle with Unit Carton - Hemp + Rose Facial Oil

```html
<!DOCTYPE html>
<html lang="en">
<head>
<meta charset="utf-8">
<title>Hemp Facial Oil – Carton and Bottle Label</title>
<link rel="stylesheet" href="https://fonts.googleapis.com/css2?family=Lobster&family=Roboto+Condensed:wght@700&family=Tinos&display=swap">
<style>
  :root {
    --bg: #7b7b7b;
    --forest: #12602d;
    --bloom: #e89ab8;
    --bloom-deep: #c94f86;
    --kraft: #d8c8a4;
    --kraft-dark: #c4b08a;
    --gold-light: #fbe79a;
    --gold: #d6a92c;
    --gold-deep: #8a5f12;
    --copper: #b9713d;
    --copper-dark: #7a4220;
    --ink: #1b1b1b;
    --title: #b0861f;
    --leaf: #1f7a34;
  }
  * { box-sizing: border-box; margin: 0; padding: 0; }
  html, body { width: 1200px; height: 945px; overflow: hidden; }
  body { background: var(--bg); position: relative; font-family: "Roboto Condensed", sans-serif; }

  .carton { position: absolute; left: 130px; top: 150px; display: flex; }
  .carton-panel { width: 270px; height: 640px; position: relative; background: var(--kraft); display: flex; flex-direction: column; }
  .carton-panel + .carton-panel { border-left: 1px solid var(--kraft-dark); }

  .floral-band { width: 100%; height: 200px; background: var(--forest); position: relative; }
  .floral-art { position: absolute; left: 6px; right: 6px; top: 28px; height: 130px; border-radius: 40px;
    background: radial-gradient(ellipse at 40% 50%, var(--bloom) 0%, var(--bloom-deep) 55%, var(--forest) 78%); }
  .badge { position: absolute; right: 14px; bottom: -22px; width: 62px; height: 62px; border-radius: 50%;
    border: 2px solid rgba(255,255,255,.6); background: rgba(255,255,255,.12); }

  .gold-rule { width: 100%; height: 9px; background: linear-gradient(180deg, var(--gold-light), var(--gold) 50%, var(--gold-deep)); }

  .copy { padding: 18px 14px; font-family: "Tinos", serif; font-size: 10.5px; line-height: 1.32; color: var(--ink); text-align: justify; }
  .copy p + p { margin-top: 22px; }

  .front { align-items: center; text-align: center; }
  .leaf-row { width: 230px; height: 58px; margin-top: 24px;
    background: linear-gradient(90deg, var(--kraft), var(--leaf) 20%, var(--leaf) 80%, var(--kraft)); border-radius: 30px; opacity: .85; }

  .wordmark { font-family: "Roboto Condensed", sans-serif; font-weight: 700; font-size: 52px; line-height: 1;
    letter-spacing: 2px; color: var(--title); }
  .front .wordmark { margin-top: 30px; }

  .name-band { width: 100%; height: 52px; margin-top: 22px; display: flex; align-items: center; justify-content: center;
    background: linear-gradient(180deg, var(--gold-light), var(--gold) 45%, var(--gold-deep));
    border-top: 2px solid var(--gold-deep); border-bottom: 2px solid var(--gold-deep); }
  .product-name { font-family: "Lobster", cursive; font-size: 30px; color: #2a1a06; }

  .ingredient-tag { margin-top: 26px; padding: 5px 16px; border-radius: 6px;
    background: linear-gradient(180deg, #d99a62, var(--copper)); border: 1.5px solid var(--copper-dark);
    font-family: "Lobster", cursive; font-size: 13px; color: #2d1606; }
  .skin-type { margin-top: 24px; font-size: 15px; font-weight: 700; color: var(--ink); }
  .volume { margin-top: 22px; font-size: 15px; font-weight: 700; color: var(--ink); }

  .label { position: absolute; left: 700px; top: 240px; width: 380px; height: 470px; background: var(--kraft);
    display: flex; flex-direction: column; align-items: center; text-align: center; }
  .label .leaf-mark { width: 64px; height: 48px; margin-top: 22px; border-radius: 50% 50% 40% 40%; background: var(--leaf); opacity: .9; }
  .label .wordmark { margin-top: 14px; font-size: 56px; }
  .label .name-band { height: 56px; margin-top: 20px; }
  .label .product-name { font-size: 32px; }
  .label .ingredient-tag { margin-top: 20px; }
  .label .skin-type { margin-top: 20px; }
  .label .volume { margin-top: 16px; margin-bottom: auto; }
</style>
</head>
<body>
  <section class="carton" aria-label="Unit carton">
    <div class="carton-panel side">
      <div class="floral-band">
        <div class="floral-art" role="img" aria-label="Illustration of pink peonies and blossoms with green sprigs"></div>
      </div>
      <div class="gold-rule"></div>
      <div class="copy">
        <p>Dummy text is also used to demonstrate the appearance of different typefaces and layouts, and in general the content of text is nonsensical. Due to its widespread use as filler text for layouts, non-readability is of great importance: human perception is tuned to recognize certain patterns and repetitions in texts.</p>
        <p>Dummy text is also used to demonstrate the appearance of different typefaces and layouts, and in general the content of text is nonsensical. Due to its widespread use as filler text for layouts, non-readability is of great importance: human perception is tuned to recognize certain patterns and repetitions in texts.</p>
      </div>
    </div>
    <div class="carton-panel front">
      <div class="floral-band">
        <div class="floral-art" role="img" aria-label="Illustration of pink peonies and blossoms with green sprigs"></div>
        <div class="badge" aria-hidden="true"></div>
      </div>
      <div class="gold-rule"></div>
      <div class="leaf-row" role="img" aria-label="Row of green hemp leaf illustrations"></div>
      <h1 class="wordmark">HEMP</h1>
      <div class="name-band"><span class="product-name">Facial Oil</span></div>
      <div class="ingredient-tag">With Hemp Oil and Rose</div>
      <div class="skin-type">ALL SKIN TYPE</div>
      <div class="volume">1 fl. Oz 30ml e</div>
    </div>
  </section>

  <section class="label" aria-label="Dropper bottle label">
    <div class="gold-rule"></div>
    <div class="leaf-mark" role="img" aria-label="Green hemp leaf illustration"></div>
    <h2 class="wordmark">HEMP</h2>
    <div class="name-band"><span class="product-name">Facial Oil</span></div>
    <div class="ingredient-tag">With Hemp Oil and Rose</div>
    <div class="skin-type">ALL SKIN TYPE</div>
    <div class="volume">1 fl. Oz 30ml e</div>
    <div class="gold-rule"></div>
  </section>
</body>
</html>
```